Harbor Wellness Partners -Postcard Design

New Post Card design for a new company based in Florida called "Harbor Wellness Partners". Our website is www.harborwellnesspartners-example.com, our phone is 855-HARBR22 (855-427-2722). We offer a no fee service to help our clients find suitable alcohol/drug abuse/addition treatment so that they can attain LONG-TERM recovery.
The facilities we work with have been hand chosen by us after a rigorous interview process.
We have facilities that use various approaches to suit the needs of the client wanting Long-Term Recovery. Evidence based, 12-step based, christian based, and alternative healing based.
Feel free to add a "tag line" that you think will catch attention. We use..."We help our clients drop anchor in Long-Term Recovery". "Call 1-855-HARBR22 before you have to call 911". "Long-Term recovery is our goal, not temporary sobriety."
We interview the treatment facilities to ensure that top treatment is given to our clients, we don't put there where they will not get the care promised.
Some services we can place for are: Interventions, Detox, Partial Hospitalization Program (PHP), Intensive Out Patient (IOP), Out Patient (OP), Sober Living Communities.
Several facilities with several approaches to treatment & recovery.

I am not a designer, so leaving entire design options open (eg...colors, graphics, fonts, etc....) Postcard size will be either 6 x 4 or 7 x 5.

Target Market(s)

Target Market for these postcards are treatment facilities & potential clients around the country. To give them someone to call for help in placing alcoholics & addicting into treatment facilities with different approaches.

Industry/Entity Type

It Company

Requirements
Must have
• THESE DO NOT HAVE TO BE EXACT WORDING!!
• The facilities we work with have been hand chosen by us after a rigorous interview process.
• Treatment programs: Detox, In-Patient, Partial Hospitalization Program (PHP), Intensive out patient (IOP), Out Patient, Sober Living Communities.
• We have facilities that use various approaches to suit the needs of the client wanting Long-Term Recovery. Evidence based, 12-step based, christian based, and alternative healing based.

```html
<!DOCTYPE html>
<html lang="en">
<head>
<meta charset="utf-8">
<title>Harbor Wellness Partners – Postcard</title>
<link rel="stylesheet" href="https://fonts.googleapis.com/css2?family=Crimson+Text:wght@400;600;700&family=Marcellus&display=swap">
<style>
  :root{
    --blue:#3f79c1;
    --green:#5db443;
    --white:#ffffff;
    --ink:#1f2a2a;
    --stage:#555759;
    --silver-hi:#f7f7f7;
    --silver-lo:#c9c9c9;
  }
  *{box-sizing:border-box;margin:0;padding:0}
  html,body{width:770px;height:1200px;overflow:hidden}
  body{background:var(--stage);position:relative;font-family:"Crimson Text",Georgia,serif}

  .card{position:absolute;background:var(--white);overflow:hidden}
  .card--front{left:44px;top:55px;width:662px;height:513px}
  .card--back{left:47px;top:621px;width:660px;height:512px}
  .card__shapes{position:absolute;inset:0}

  /* front */
  .brand-leaf{position:absolute;left:29px;top:60px;width:237px;height:195px;background:var(--green);
    border-radius:6px 80px 6px 80px;display:flex;align-items:center;padding-left:22px;gap:14px}
  .brand-leaf__dot{width:64px;height:64px;border-radius:50%;background:#222;flex:none}
  .brand-leaf__name{font-family:"Crimson Text",Georgia,serif;font-weight:400;color:var(--ink);
    font-size:20px;line-height:18px;text-transform:uppercase;letter-spacing:.3px}
  .photo{position:absolute;border:4px solid var(--white);box-shadow:0 1px 3px rgba(0,0,0,.25)}
  .photo--pharmacy{left:276px;top:34px;width:270px;height:224px;border-radius:46px 6px 46px 6px;
    background:linear-gradient(135deg,#d9dde0,#eef0f1 55%,#c7ccd0)}
  .photo--doctor{left:22px;top:266px;width:246px;height:208px;border-radius:6px 6px 60px 6px;
    background:linear-gradient(135deg,#e8ecef,#9fb4d6 55%,#d7b9a6)}
  .headline{position:absolute;left:278px;top:360px;color:var(--white);font-family:"Marcellus",Georgia,serif;
    font-size:27px;line-height:32px;letter-spacing:.5px;font-weight:400}
  .headline__big{display:block;font-size:38px;line-height:46px;letter-spacing:1px}

  /* back */
  .about-tab{position:absolute;left:0;top:24px;width:143px;height:32px;border-radius:0 16px 16px 0;
    background:linear-gradient(var(--silver-hi),var(--silver-lo));box-shadow:0 1px 3px rgba(0,0,0,.4);
    font-weight:700;font-size:22px;line-height:32px;padding-left:26px;color:var(--ink)}
  .about-text{position:absolute;left:25px;top:68px;width:334px;color:var(--white);font-size:13.2px;line-height:15.2px}
  .about-goal{position:absolute;left:25px;top:240px;color:var(--white);font-size:13.5px;font-weight:700}
  .photo--team{left:23px;top:286px;width:168px;height:93px;border:3px solid var(--green);border-radius:30px 4px 4px 4px;
    background:linear-gradient(135deg,#f1efe9,#b9c7d6 50%,#8fa6c4)}
  .photo--care{left:199px;top:286px;width:164px;height:93px;border:3px solid var(--green);border-radius:30px 4px 30px 4px;
    background:linear-gradient(135deg,#dfe5ea,#7fa6d3 50%,#e2d8cc)}
  .call-pill{position:absolute;left:93px;top:424px;width:228px;height:63px;border-radius:32px;background:var(--green);
    color:var(--ink);text-align:center;font-weight:700;padding-top:7px}
  .call-pill__number{display:block;font-size:19px;line-height:24px}
  .call-pill__note{display:block;font-size:15.5px;line-height:22px;font-weight:600}
  .website{position:absolute;left:93px;top:492px;width:228px;text-align:center;color:var(--white);font-size:12px;line-height:14px}

  .facility-note{position:absolute;left:444px;top:18px;width:196px;color:var(--ink);font-size:11.5px;line-height:13px}
  .facility-note strong{font-weight:700}
  .program-list{position:absolute;right:20px;top:360px;width:170px;text-align:right;color:var(--ink);
    font-size:11.5px;line-height:14px;list-style:none}
  .program-list__title{font-weight:700;font-size:12.5px}

  .stamp-box{position:absolute;left:574px;top:96px;width:50px;height:56px;border:1.5px solid #333}
  .address-line{position:absolute;left:431px;width:199px;height:0;border-top:1.2px solid #333}
</style>
</head>
<body>

<section class="card card--front" aria-label="Postcard front">
  <svg class="card__shapes" viewBox="0 0 662 513" aria-hidden="true">
    <path d="M0,343 L250,350 C390,345 535,250 548,0 L560,0 C612,180 600,380 540,513 L0,513 Z" fill="var(--blue)"/>
    <path d="M548,0 L560,0 C612,180 600,380 540,513 L490,513 C580,380 600,180 548,0 Z" fill="var(--green)"/>
    <path d="M572,0 C626,180 616,380 560,513" fill="none" stroke="var(--blue)" stroke-width="2.5"/>
    <path d="M586,0 C642,180 636,380 585,513" fill="none" stroke="var(--green)" stroke-width="2.5"/>
  </svg>
  <div class="brand-leaf">
    <span class="brand-leaf__dot"></span>
    <span class="brand-leaf__name">Harbor<br>Wellness<br>Partners</span>
  </div>
  <div class="photo photo--pharmacy" role="img" aria-label="Photo of pharmacists in white coats in a pharmacy"></div>
  <div class="photo photo--doctor" role="img" aria-label="Photo of a doctor holding out a stethoscope"></div>
  <h1 class="headline">DROP ANCHOR IN<br>LONG-TERM<span class="headline__big">RECOVERY</span></h1>
</section>

<section class="card card--back" aria-label="Postcard back">
  <svg class="card__shapes" viewBox="0 0 660 512" aria-hidden="true">
    <path d="M0,0 L405,0 C365,200 395,400 460,512 L0,512 Z" fill="var(--blue)"/>
    <path d="M405,0 L414,0 C380,200 425,400 505,512 L460,512 C395,400 365,200 405,0 Z" fill="var(--green)"/>
    <path d="M424,0 C392,200 445,400 530,512" fill="none" stroke="var(--blue)" stroke-width="2.5"/>
    <path d="M434,0 C404,200 460,400 548,512" fill="none" stroke="var(--green)" stroke-width="2.5"/>
  </svg>
  <h2 class="about-tab">About Us</h2>
  <p class="about-text">We offer a no fee service to help our clients find suitable alcohol/ drug abuse/addition treatment so that they can attain LONG-TERM recovery. We are different in the sense that we don't just get them into a treatment program, we become their "coach" from the beginning and accompany them though the process -- LONG TERM. We will be available to each client for as long as they keep our contact information, even if it is 10 years after the first appointment. Age doesn't matter, we will work with 12 year olds or 75 year olds. From any demographic in the USA.</p>
  <p class="about-goal">Long-Term recovery is our goal, not temporary sobriety.</p>
  <div class="photo photo--team" role="img" aria-label="Photo of a smiling medical team"></div>
  <div class="photo photo--care" role="img" aria-label="Photo of a nurse caring for an elderly patient"></div>
  <p class="call-pill"><span class="call-pill__number">Call 1-855-HARBR22</span><span class="call-pill__note">before you have to call 911</span></p>
  <p class="website">www.harborwellnesspartners-example.com</p>

  <p class="facility-note"><strong>Hand-chosen facilities</strong> – every one passes our rigorous interview process. Approaches: evidence based, 12-step based, christian based and alternative healing based.</p>

  <ul class="program-list">
    <li class="program-list__title">Programs we place for</li>
    <li>Partial Hospitalization (PHP)</li>
    <li>Intensive Out Patient (IOP)</li>
    <li>Sober Living Communities</li>
    <li>In-Patient · Out Patient</li>
    <li>Detox</li>
  </ul>

  <div class="stamp-box"></div>
  <div class="address-line" style="top:287px"></div>
  <div class="address-line" style="top:311px"></div>
  <div class="address-line" style="top:340px"></div>
</section>

</body>
</html>
```